We need a new design for our construction website

We need a new website for our wordpress site kerrowmade.co.nz

It needs to be only a few pages but sleek in design and responsive, beautifully showcasing our images and video. Currently we have
1. home
2. about us
3. contact
We need either a front page that is designed much better to showcase more content, or potentially a projects page which has images from our builds. We don't have a lot of content so the content we do have needs to be maximised by image, rather than project.

Target Market(s)

High end residential construction and renovation projects, people wanting to build a nice home, clients based in Mount Maunganui, Tauranga.

Coding

Font styles to use
Sans Serif

Colors

Designer to choose only greyscale colors for use in the design.

Requirements
Must have
• A sleek design, architectural

```html
<!DOCTYPE html>
<html lang="en">
<head>
<meta charset="utf-8">
<title>Kerrowmade — Construction</title>
<link rel="stylesheet" href="https://fonts.googleapis.com/css2?family=Montserrat:wght@400;500;600;700;800&family=Roboto:wght@400;500;700;900&display=swap">
<style>
:root{
  --accent:#7a7a7a;
  --accent-light:#a6a6a6;
  --heading:#141414;
  --ink:#1f1f1f;
  --night:#222222;
  --paper:#f7f7f7;
  --grey:#7b7b7b;
  --text:#333333;
  --card:#e9e9e9;
  --white:#ffffff;
}
*{box-sizing:border-box;margin:0;padding:0}
html,body{width:1200px;height:3817px;overflow:hidden}
body{position:relative;font-family:"Montserrat",sans-serif;color:var(--text);background:var(--paper)}
.abs{position:absolute}
section{position:absolute;left:0;width:1200px;overflow:hidden}
.btn{position:absolute;background:var(--accent);color:var(--white);font-family:"Montserrat",sans-serif;font-weight:600;text-transform:uppercase;display:flex;align-items:center;justify-content:center;letter-spacing:.02em}
.accent{color:var(--accent)}
.dark .accent{color:var(--accent-light)}
.ghost{position:absolute;font-family:"Montserrat",sans-serif;font-weight:800;color:transparent;-webkit-text-stroke:1.5px rgba(170,170,170,.22);white-space:nowrap;line-height:1}
.dark .ghost{-webkit-text-stroke:1.5px rgba(255,255,255,.06)}
.photo{position:absolute}

/* hero */
.hero{top:0;height:516px;background:var(--night)}
.hero-photo{left:600px;top:0;width:600px;height:516px;background:linear-gradient(160deg,#8a8a8a 0%,#5e5e5e 30%,#3c3c3c 60%,#6a6a6a 85%,#2e2e2e 100%)}
.logo-box{left:0;top:0;width:333px;height:95px;background:var(--accent);display:flex;align-items:center;padding-left:120px;gap:12px}
.logo-mark{width:26px;height:26px;border:2px solid var(--white)}
.logo-name{color:var(--white);font-size:15px;letter-spacing:.34em;font-weight:500}
.menu-box{left:1080px;top:0;width:120px;height:95px;background:var(--accent)}
.eyebrow{font-size:14px;font-weight:500;color:var(--white);text-transform:uppercase}
.hero-title{left:120px;top:148px;font-family:"Roboto",sans-serif;font-weight:700;font-size:48px;color:var(--white)}
.hero-sub{left:120px;top:396px;font-size:22px;font-weight:600;color:var(--white)}

/* offer */
.offer{top:516px;height:514px;background:var(--paper)}
.sec-eyebrow{left:0;width:1200px;text-align:center;font-size:19px;color:var(--accent);font-weight:500}
.sec-title{left:0;width:1200px;text-align:center;font-size:48px;font-weight:800;color:var(--heading);line-height:1}
.service{position:absolute;top:192px;width:240px}
.service svg{display:block;width:56px;height:50px}
.service h3{font-family:"Roboto",sans-serif;font-weight:500;font-size:22px;color:var(--ink);margin-top:18px;white-space:nowrap}
.service p{font-family:"Roboto",sans-serif;font-size:13.5px;line-height:15px;color:var(--grey);margin-top:12px;height:62px;width:192px}
.service .btn{position:static;width:115px;height:27px;font-size:10px;margin-top:36px}

/* dark bands */
.dark{background:var(--night)}
.band-title{left:0;width:1200px;text-align:center;font-size:48px;font-weight:800;color:var(--white);line-height:1}
.band-lead{left:190px;width:820px;text-align:center;font-size:14px;line-height:21px;color:var(--white);font-weight:500}
.work{top:1030px;height:517px}
.work .photo{top:203px;width:216px;height:245px}

/* welcome */
.welcome{top:1547px;height:520px;background:var(--paper)}
.feature-card{position:absolute;top:50px;width:222px;height:422px;background:linear-gradient(180deg,#3c3c3c 0%,#2a2a2a 55%,#444444 100%);text-align:center;color:var(--white)}
.feature-card svg{margin-top:96px}
.feature-card h4{font-family:"Montserrat",sans-serif;font-weight:500;font-size:21px;color:var(--accent-light);margin-top:14px}
.feature-card p{font-size:12.5px;line-height:20px;margin:10px auto 0;width:204px;font-weight:400}
.feature-card .btn{left:46px;top:329px;width:130px;height:33px;font-size:12px}
.wel-title{left:655px;top:52px;font-size:50px;font-weight:800;color:var(--heading);line-height:1}
.wel-sub{left:655px;top:107px;font-size:37px;font-weight:800;color:var(--accent);line-height:1}
.wel-text{left:657px;top:168px;width:440px;font-size:14.2px;line-height:24.5px;color:var(--text);font-weight:500}
.checks{position:absolute;left:660px;top:304px;list-style:none}
.checks li{display:flex;align-items:center;gap:14px;font-size:14px;height:36px;color:var(--text);font-weight:500}

/* projects */
.projects{top:2067px;height:711px}
.filters{position:absolute;top:182px;left:0;width:1200px;height:28px}
.filters span{position:absolute;top:0;height:28px;display:flex;align-items:center;font-size:12.5px;color:var(--white);font-weight:500}
.filters .active{background:var(--accent);padding:0 10px}

/* reviews */
.reviews{top:2778px;height:551px;background:var(--paper)}
.review{position:absolute;border-radius:14px;font-size:11.5px;line-height:19px}
.review .quote{position:absolute;left:16px;top:18px;font-family:"Roboto",sans-serif;font-weight:900;font-size:56px;line-height:.7}
.review p{position:absolute;left:58px;top:30px;right:18px}
.review.light{background:var(--card);color:#8a8a8a;width:270px;height:207px;top:172px}
.review.light .quote{color:#b3b3b3}
.review.feature{background:var(--night);color:var(--white);left:440px;top:154px;width:314px;height:240px;font-size:12.5px;line-height:21px}
.review.feature .quote{color:var(--white)}
.review.feature::after{content:"";position:absolute;left:147px;bottom:-10px;border:10px solid transparent;border-bottom:0;border-top-color:var(--night)}
.avatar{position:absolute;width:66px;height:66px;border-radius:50%;background:radial-gradient(circle at 50% 40%,#c4c4c4,#7e7e7e)}
.name{position:absolute;width:200px;text-align:center;font-size:12.5px;font-weight:700;color:var(--ink);text-transform:uppercase}

/* contact */
.contact{top:3329px;height:488px}
.contact-head{left:0;width:1200px;text-align:center;top:42px;font-size:21px;font-weight:500;color:var(--accent-light);text-transform:uppercase}
.contact-lead{left:200px;width:800px;text-align:center;top:84px;font-size:14.5px;line-height:22px;color:var(--white);font-weight:500}
.foot-logo{left:127px;top:150px;display:flex;align-items:center;gap:14px}
.foot-logo .logo-mark{width:32px;height:32px}
.foot-logo .logo-name{font-size:17px}
.info-title{left:128px;top:210px;font-size:19px;color:var(--accent-light);font-weight:500}
.info{position:absolute;left:130px;display:flex;align-items:flex-start;gap:12px;color:var(--white);font-size:12.5px;font-weight:500;line-height:15px}
.follow{left:128px;top:384px;font-size:17px;color:var(--white);font-weight:600}
.social{position:absolute;top:416px;width:31px;height:31px;background:#6e6e6e}
.field{position:absolute;left:606px;width:465px;border:1px solid #c8c8c8;color:var(--white);font-size:12px;padding:9px 10px;font-weight:500}
.contact .btn{left:935px;top:416px;width:137px;height:34px;font-size:13px}
</style>
</head>
<body>

<section class="hero">
  <div class="photo hero-photo" role="img" aria-label="Construction site with a worker in a hi-vis vest seen from above"></div>
  <div class="abs logo-box"><span class="logo-mark"></span><span class="logo-name">KERROWMADE</span></div>
  <div class="abs menu-box">
    <svg class="abs" style="left:47px;top:36px" width="26" height="22" viewBox="0 0 26 22"><path d="M4 3h20M1 11h23M10 19h14" stroke="#fff" stroke-width="2.6" stroke-linecap="round"/></svg>
  </div>
  <div class="abs eyebrow" style="left:120px;top:125px">Explore the features</div>
  <div class="abs hero-title">STAYING AHEAD</div>
  <svg class="abs" style="left:0;top:0" width="1200" height="516" viewBox="0 0 1200 516">
    <defs><clipPath id="rightHalf"><rect x="600" y="0" width="600" height="516"/></clipPath></defs>
    <text x="232" y="333" font-family="Roboto,sans-serif" font-weight="700" font-size="170" fill="none" stroke="rgba(255,255,255,.12)" stroke-width="2">SCHEDULE</text>
    <text x="232" y="333" font-family="Roboto,sans-serif" font-weight="700" font-size="170" fill="#fff" clip-path="url(#rightHalf)">SCHEDULE</text>
  </svg>
  <div class="abs eyebrow" style="left:120px;top:380px">Explore the features</div>
  <div class="abs hero-sub">Experience by more than 20 years</div>
  <div class="btn" style="left:121px;top:450px;width:155px;height:39px;font-size:13px">Read more</div>
</section>

<section class="offer">
  <div class="ghost" style="left:830px;top:22px;font-size:110px">WHAT WE</div>
  <div class="abs sec-eyebrow" style="top:50px">EXPLORE THE FEATURES</div>
  <div class="abs sec-title" style="top:74px">WHAT WE OFFER</div>

  <div class="service" style="left:126px">
    <svg viewBox="0 0 56 50"><path d="M4 24L28 4l24 20M10 19v27h36V19M22 46V31h12v15" fill="none" stroke="#7a7a7a" stroke-width="2.5" stroke-linejoin="round"/></svg>
    <h3>Design and Build</h3>
    <p>The Design and Build process streamlines your home construction project ensuring your architect or designer ....</p>
    <div class="btn">Read more</div>
  </div>
  <div class="service" style="left:351px">
    <svg viewBox="0 0 56 50"><path d="M6 44L30 20M36 6l8 8-6 6-8-8zM10 6l34 34M40 44l6-6M8 10l-4-4 4-4 4 4" fill="none" stroke="#7a7a7a" stroke-width="2.5" stroke-linecap="round"/></svg>
    <h3>Renovations &amp; Additions</h3>
    <p>Improving the layout and functionality of your home doesn't mean having to build from scratch, renovations ....</p>
    <div class="btn">Read more</div>
  </div>
  <div class="service" style="left:609px">
    <svg viewBox="0 0 56 50"><path d="M4 4h6v42H4zM10 10h40v36H10M18 38l22-22 4 4-22 22h-4z" fill="none" stroke="#7a7a7a" stroke-width="2.3" stroke-linejoin="round"/></svg>
    <h3>Project Management</h3>
    <p>We specialise in managing your entire build project. From liaising with your designer, engineers, advising you the best building ....</p>
    <div class="btn">Read more</div>
  </div>
  <div class="service" style="left:853px">
    <svg viewBox="0 0 56 50"><path d="M4 46h44M8 46V24h12v22M20 46V14h14v32M34 46V20h12v26M24 8h6v6M12 30h4M12 36h4M24 22h6M24 30h6M38 28h4M38 36h4" fill="none" stroke="#7a7a7a" stroke-width="2.3"/></svg>
    <h3>Build Smarter</h3>
    <p>We are passionate about building smarter, even better than the building codeWhen it comes to energy efficiency ...</p>
    <div class="btn">Read more</div>
  </div>
</section>

<section class="work dark">
  <div class="ghost" style="left:-20px;top:20px;font-size:120px">OUR WORK</div>
  <div class="abs band-title" style="top:40px">OUR <span class="accent">WORK</span></div>
  <div class="abs band-lead" style="top:97px">Lorem ipsum dolor sit amet, consectetur adipiscing elit, sed do eiusmod temporesse cillum dolore eu fugiat nulla eu fugiat nulla pariatur.Lorem ipsum dolor sit amet, consecteture.</div>
  <div class="photo" style="left:138px;background:linear-gradient(160deg,#5a5a5a,#e2e2e2 55%,#3a3a3a)" role="img" aria-label="Worker in hi-vis vest holding rolled building plans"></div>
  <div class="photo" style="left:375px;background:linear-gradient(170deg,#cfcfcf,#6e6e6e 45%,#9a9a9a 75%,#7b7b7b)" role="img" aria-label="Timber frame house under construction with a telehandler"></div>
  <div class="photo" style="left:612px;background:linear-gradient(180deg,#8a8a8a,#d2d2d2 45%,#404040 100%)" role="img" aria-label="Tower cranes above a high-rise under construction"></div>
  <div class="photo" style="left:847px;background:linear-gradient(180deg,#8c8c8c,#c4c4c4 55%,#6a6a6a 80%,#3f3f3f)" role="img" aria-label="Tower crane beside a brick building under construction"></div>
</section>

<section class="welcome">
  <div class="ghost" style="left:600px;top:10px;font-size:110px">WELCOME</div>
  <div class="feature-card" style="left:123px" role="img" aria-label="Drafting desk with plans behind the card">
    <svg width="50" height="52" viewBox="0 0 50 52"><path d="M6 50V2M6 4h34l-8 10 8 10H6" fill="none" stroke="#fff" stroke-width="2"/></svg>
    <h4>PROJECT</h4>
    <p>Improving the layout and functionality of your home doesn't mean having to build from scratch, renovations</p>
    <div class="btn">Read more</div>
  </div>
  <div class="feature-card" style="left:375px" role="img" aria-label="Dim office workspace behind the card">
    <svg width="56" height="56" viewBox="0 0 56 56"><circle cx="28" cy="22" r="11" fill="none" stroke="#fff" stroke-width="2"/><path d="M12 24v-4a16 16 0 0132 0v4M10 20h4v10h-4zM42 20h4v10h-4zM44 30q0 6-12 6M8 54q2-14 20-14t20 14" fill="none" stroke="#fff" stroke-width="2"/></svg>
    <h4>CREATIVE</h4>
    <p>Improving the layout and functionality of your home doesn't mean having to build from scratch, renovations</p>
    <div class="btn">Read more</div>
  </div>
  <div class="abs wel-title">WELCOME</div>
  <div class="abs wel-sub">FOR PROFESSIONALS</div>
  <p class="abs wel-text">The Design and Build process streamlines your home construction project ensuring your architect or designer and builder are on the same page from day one meaning you get the dream home you've always wanted.</p>
  <ul class="checks">
    <li><svg width="18" height="18" viewBox="0 0 18 18"><circle cx="9" cy="9" r="7.5" fill="none" stroke="#7a7a7a" stroke-width="2"/><path d="M5.5 9l2.5 2.5 4.5-5" fill="none" stroke="#7a7a7a" stroke-width="2"/></svg>Lorem ipsum dolor sitconsectetur adipiscing</li>
    <li><svg width="18" height="18" viewBox="0 0 18 18"><circle cx="9" cy="9" r="7.5" fill="none" stroke="#7a7a7a" stroke-width="2"/><path d="M5.5 9l2.5 2.5 4.5-5" fill="none" stroke="#7a7a7a" stroke-width="2"/></svg>Lorem ipsum dolor sit ametadipiscing</li>
    <li><svg width="18" height="18" viewBox="0 0 18 18"><circle cx="9" cy="9" r="7.5" fill="none" stroke="#7a7a7a" stroke-width="2"/><path d="M5.5 9l2.5 2.5 4.5-5" fill="none" stroke="#7a7a7a" stroke-width="2"/></svg>Lorem dolor sit amet, consectetur adipiscing</li>
    <li><svg width="18" height="18" viewBox="0 0 18 18"><circle cx="9" cy="9" r="7.5" fill="none" stroke="#7a7a7a" stroke-width="2"/><path d="M5.5 9l2.5 2.5 4.5-5" fill="none" stroke="#7a7a7a" stroke-width="2"/></svg>Ipsum dolor sit amet, consectetur adipiscing</li>
    <li><svg width="18" height="18" viewBox="0 0 18 18"><circle cx="9" cy="9" r="7.5" fill="none" stroke="#7a7a7a" stroke-width="2"/><path d="M5.5 9l2.5 2.5 4.5-5" fill="none" stroke="#7a7a7a" stroke-width="2"/></svg>Lorem ipsum dolor sitconsectetur adipiscing</li>
  </ul>
</section>

<section class="projects dark">
  <div class="ghost" style="left:-30px;top:20px;font-size:120px">PROJECTS</div>
  <div class="abs band-title" style="top:41px">OUR <span class="accent">PROJECTS</span></div>
  <div class="abs band-lead" style="top:110px">Lorem ipsum dolor sit amet, consectetur adipiscing elit, sed do eiusmod temporesse cillum dolore eu fugiat nulla eu fugiat nulla pariatur.Lorem ipsum dolor sit amet, consecteture.</div>
  <div class="filters">
    <span class="active" style="left:341px">SHOW ALL</span>
    <span style="left:446px">BUILDINGS</span>
    <span style="left:542px">INTERIOR DESIGN</span>
    <span style="left:683px">ISOLATION</span>
    <span style="left:778px">PLUMBING</span>
  </div>
  <div class="photo" style="left:123px;top:244px;width:470px;height:397px;background:linear-gradient(180deg,#262626 0%,#2e2e2e 40%,#8a8a8a 65%,#303030 100%)" role="img" aria-label="Historic opera house lit at night"></div>
  <div class="photo" style="left:599px;top:244px;width:237px;height:194px;background:radial-gradient(circle at 50% 45%,#f5f5f5 0%,#b4b4b4 25%,#5a5a5a 60%,#262626 100%)" role="img" aria-label="Looking up through a tall building atrium toward the sky"></div>
  <div class="photo" style="left:843px;top:244px;width:237px;height:194px;background:linear-gradient(180deg,#c2c2c2,#979797 50%,#646464 80%,#575757)" role="img" aria-label="Curved concrete boat lift structure above a canal"></div>
  <div class="photo" style="left:599px;top:447px;width:237px;height:194px;background:linear-gradient(180deg,#bcbcbc,#737373 45%,#5a5a5a 85%,#404040)" role="img" aria-label="Gothic stone church among trees"></div>
  <div class="photo" style="left:843px;top:447px;width:237px;height:194px;background:linear-gradient(180deg,#939393,#6a6a6a 40%,#bdbdbd 70%,#767676)" role="img" aria-label="Residential tower wrapped in scaffolding with a crane"></div>
</section>

<section class="reviews">
  <div class="ghost" style="left:600px;top:20px;font-size:130px">CUSTOMER</div>
  <div class="abs sec-title" style="top:32px">CUSTOMER <span class="accent">REVIEWS</span></div>
  <div class="review light" style="left:121px"><span class="quote">❝</span><p style="text-align:center">Nemo enim ipsam voluptatem quia voluptas sit aspernatur aut odit aut fugit, sed quia consequuntur magni dolores eos qui ratione voluptatem sequi nesciunt. Neque porro quisqu-am est, qui dolorem ipsum quia dolor sit amet, consectetur, adipisci velit,</p></div>
  <div class="review feature"><span class="quote">❝</span><p>Nemo enim ipsam voluptatem quia voluptas sit aspernatur aut odit aut fugit, sed quia consequuntur magni dolores eos qui ratione voluptatem sequi nesciunt. Neque porro quisquam est, qui dolorem ipsum quia dolor sit amet, con-sectetur, adipisci velit,</p></div>
  <div class="review light" style="left:807px"><span class="quote">❝</span><p style="text-align:center">Nemo enim ipsam voluptatem quia voluptas sit aspernatur aut odit aut fugit, sed quia consequuntur magni dolores eos qui ratione voluptatem sequi nesciunt. Neque porro quisqu-am est, qui dolorem ipsum quia dolor sit amet, consectetur, adipisci velit,</p></div>
  <div class="avatar" style="left:225px;top:404px" role="img" aria-label="Customer portrait"></div>
  <div class="avatar" style="left:564px;top:427px" role="img" aria-label="Customer portrait"></div>
  <div class="avatar" style="left:903px;top:404px" role="img" aria-label="Customer portrait"></div>
  <div class="name" style="left:158px;top:480px">Aria Holt</div>
  <div class="name" style="left:497px;top:504px;color:var(--accent)">Aria Holt</div>
  <div class="name" style="left:836px;top:480px">Aria Holt</div>
</section>

<section class="contact dark">
  <div class="abs contact-head">Contact us for a free no obligation chat about your building project</div>
  <div class="abs contact-lead">We'd love to hear about your building project and discuss how Kerrowmade can help you design and build your dream home smarter.</div>
  <div class="abs foot-logo"><span class="logo-mark"></span><span class="logo-name">KERROWMADE</span></div>
  <div class="abs info-title">Contact info</div>
  <div class="info" style="top:252px"><svg width="16" height="16" viewBox="0 0 16 16"><path d="M3 1l3 3-2 2q2 4 6 6l2-2 3 3-2 2Q5 14 1 3z" fill="none" stroke="#fff" stroke-width="1.3"/></svg>021 555 0184</div>
  <div class="info" style="top:292px"><svg width="16" height="14" viewBox="0 0 16 14"><rect x="1" y="2" width="14" height="10" fill="none" stroke="#fff" stroke-width="1.3"/><path d="M1 2l7 6 7-6" fill="none" stroke="#fff" stroke-width="1.3"/></svg>studio@kerrowmade.co.nz</div>
  <div class="info" style="top:324px"><svg width="16" height="18" viewBox="0 0 16 18"><path d="M8 17s6-6 6-10A6 6 0 002 7c0 4 6 10 6 10z" fill="none" stroke="#fff" stroke-width="1.3"/><circle cx="8" cy="7" r="2" fill="none" stroke="#fff" stroke-width="1.3"/></svg><span>14 Harbour Lane<br>3116 Mount Maunganui</span></div>
  <div class="abs follow">Follow us on</div>
  <div class="social" style="left:130px" aria-label="Social link"></div>
  <div class="social" style="left:185px;background:#8c8c8c" aria-label="Social link"></div>
  <div class="social" style="left:240px;background:#5e5e5e" aria-label="Social link"></div>
  <div class="social" style="left:295px;background:#7a7a7a" aria-label="Social link"></div>
  <div class="field" style="top:166px;height:34px">Name</div>
  <div class="field" style="top:209px;height:34px">Email</div>
  <div class="field" style="top:252px;height:34px">Phone</div>
  <div class="field" style="top:295px;height:98px">Message</div>
  <div class="btn">Send message</div>
</section>

</body>
</html>
```